business card for law firm that reflects the web site -www.MarlaQuentby.com. That is pleasant to read

We need a business card for a small law firm. Your company designed our logo - tree of life - which I can provide to the designers. The card should be on both sides. Use the coloring from the web site (www.MarlaQuentby.com) and logo (I have several formats). I am attaching the logo, but not sure what format to use.

First side name of firm: Law Office of M.K. Quentby, P.A. 4819 West Pallisor, Suite 300, Phoenix, AZ 85016, Phone: 602.555.3841, Fax: 602.555.7290, web site: www.MarlaQuentby.com, email: MQuentby@MarlaQuentby.com.
Marla K. Quentby Bankruptcy and Foreclosure Attorney & Counselor.
Back side (perhaps vertical) the logo and then Notes with lines. At the bottom: Proud to help people and small businesses file for bankruptcy protection. We are a debt relief agency.
Updates

I have several versions of the logo. Will be happy to share whatever you need. Added Sunday, April 3, 2016

Target Market(s)

everyone

Industry/Entity Type

Legal

Contact Information for Business Card

I prefer something unique (rounded edges, design that adopts my web site - www.MarlaQuentby.com.

Font styles to use
Serif

Requirements
Must have
• First side name of firm: Law Office of M.K. Quentby, P.A. 4819 West Pallisor, Suite 300, Phoenix, AZ 85016, Phone: 602.555.3841, Fax: 602.555.7290, web site: www.MarlaQuentby.com, email: MQuentby@MarlaQuentby.com.
• Marla K. Quentby Bankruptcy and Foreclosure Attorney & Counselor.
• Back side (perhaps vertical) the logo and then Notes with lines. At the bottom: Proud to help people and small businesses file for bankruptcy protection. We are a debt relief agency.
• Green and brown colors that reflect the web site: www.MarlaQuentby.com
Should not have
• Type so small that older people cannot read.

```html
<!DOCTYPE html>
<html lang="en">
<head>
<meta charset="utf-8">
<title>Law Office of M.K. Quentby, P.A. — Business Card</title>
<link href="https://fonts.googleapis.com/css2?family=Questrial&display=swap" rel="stylesheet">
<style>
  :root {
    --backdrop: #ece8e1;
    --card-cream: #e6d39c;
    --card-plum: #2b1320;
    --ink: #1a1410;
    --rule-dark: #111111;
    --paper-white: #f2f0ee;
    --rule-light: #b9aeb4;
    --logo-green: #3f7a3a;
    --shadow: rgba(40, 25, 15, 0.28);
  }
  * { box-sizing: border-box; margin: 0; padding: 0; }
  html, body {
    width: 1200px;
    height: 763px;
    overflow: hidden;
    background: var(--backdrop);
    font-family: "Questrial", "Century Gothic", sans-serif;
  }
  .canvas {
    position: relative;
    width: 1200px;
    height: 763px;
  }
  .card {
    position: absolute;
    width: 540px;
    height: 310px;
    border-radius: 6px;
    overflow: hidden;
    box-shadow: 0 10px 28px var(--shadow);
  }
  /* Front side */
  .card-front {
    left: 40px;
    top: 226px;
    background: var(--card-cream);
    color: var(--ink);
  }
  .contact-block {
    position: absolute;
    left: 80px;
    top: 20px;
    width: 290px;
    text-align: center;
    font-size: 16px;
    line-height: 1.24;
  }
  .contact-block .attorney { margin-top: 4px; }
  .contact-block .web { font-size: 13px; margin-top: 6px; line-height: 1.35; }
  .front-bar {
    position: absolute;
    right: 0;
    top: 196px;
    width: 150px;
    height: 9px;
    background: var(--rule-dark);
  }
  .front-rule {
    position: absolute;
    left: 0;
    top: 272px;
    width: 300px;
    height: 1.5px;
    background: var(--rule-dark);
  }
  /* Back side */
  .card-back {
    left: 620px;
    top: 226px;
    background: var(--card-plum);
    color: var(--paper-white);
  }
  .brand-mark {
    position: absolute;
    left: 230px;
    top: 34px;
    display: flex;
    align-items: center;
    gap: 14px;
  }
  .brand-mark .brand-name {
    font-size: 20px;
    color: var(--paper-white);
    letter-spacing: 0.5px;
  }
  .back-bar {
    position: absolute;
    left: 0;
    top: 180px;
    width: 250px;
    height: 8px;
    background: var(--paper-white);
  }
  .back-rule {
    position: absolute;
    left: 250px;
    top: 187px;
    width: 290px;
    height: 1px;
    background: var(--rule-light);
  }
  .tagline {
    position: absolute;
    left: 170px;
    top: 210px;
    width: 330px;
    text-align: center;
    font-size: 17px;
    line-height: 1.32;
  }
</style>
</head>
<body>
<main class="canvas">
  <section class="card card-front" aria-label="Front of business card">
    <div class="contact-block">
      <p class="firm">Law Office of M.K. Quentby, P.A.</p>
      <p class="address">4819 West Pallisor,<br>Suite 300, Phoenix,<br>AZ 85016,</p>
      <p class="phone">Phone: 602.555.3841,</p>
      <p class="fax">Fax: 602.555.7290,</p>
      <p class="attorney">Marla K. Quentby Bankruptcy<br>and Foreclosure Attorney<br>&amp; Counselor.</p>
      <p class="web">www.MarlaQuentby.com<br>MQuentby@MarlaQuentby.com.</p>
    </div>
    <div class="front-bar"></div>
    <div class="front-rule"></div>
  </section>

  <section class="card card-back" aria-label="Back of business card">
    <div class="brand-mark">
      <svg width="110" height="110" viewBox="0 0 110 110" aria-hidden="true">
        <circle cx="55" cy="55" r="52" fill="var(--logo-green)"/>
      </svg>
      <span class="brand-name">M.K. Quentby</span>
    </div>
    <div class="back-bar"></div>
    <div class="back-rule"></div>
    <p class="tagline">Proud to help people and small businesses file for bankruptcy protection.<br>We are a debt relief agency</p>
  </section>
</main>
</body>
</html>
```